Postcard: Live Ever Kinder

Text for front: HOW TO CHANGE THE WORLD IN ONE [note: the word "one" should be underlined] STEPHint: It's up to you...[Note: add arrow or something to indicate "turn over"]Text for back: You're going to spend your entire life with someone you can never get away from. (Guess who?) Wouldn't you rather that person #LiveEverKinder than judgmental or critical? BE the change you want to see! Visit www.LiveEverKinder-hub.com for daily Bright Pebbles and community. PLEASE JOIN US![Note: add logo to left half of back side]Font preference for text: Josefin sans

Target Market(s)

People who would be attracted to Calvera church - unitarian universalist message. It's spiritual without being overtly religious, so the target market is probably early 30s and up but ideally won't turn off Millennials (folks under 30). It should attract attention of people who are open-minded and committed to progressive social change, tired of an atmosphere of hate-mongering and divisiveness.

Requirements
Nice to have
• It would be nice to convey a sense of challenge - there is an idea of "bright pebbles" so something related to fire/sparks is appropriate. This is meant to evoke a deeper, divine love more than a sense of romantic love. This love is more fierce than fluffy! Yet it calls us to be our best selves.
Should not have
• Please avoid excessive pink - just the logo is enough, as this design needs to appeal to men as well as women.

```html
<!DOCTYPE html>
<html lang="en">
<head>
<meta charset="utf-8">
<title>Live Ever Kinder – Postcard</title>
<link rel="stylesheet" href="https://fonts.googleapis.com/css2?family=Josefin+Sans:wght@300;400;600;700&display=swap">
<style>
  :root {
    --paper: #f6f1ea;
    --wash-light: #fbf8f3;
    --wash-warm: #eee2d3;
    --wash-ember: #ecd3bf;
    --headline: #b9442c;
    --headline-shadow: rgba(90, 30, 15, 0.35);
    --divider: #ffffff;
    --ink: #1f1c1a;
    --logo-fill: #e8829f;
    --logo-name: #d9578a;
  }
  * { margin: 0; padding: 0; box-sizing: border-box; }
  html, body { width: 849px; height: 1200px; overflow: hidden; background: var(--paper); }
  .postcard {
    position: relative;
    width: 849px;
    height: 1200px;
    overflow: hidden;
    font-family: "Josefin Sans", sans-serif;
    background:
      radial-gradient(ellipse 320px 240px at 90px 150px, var(--wash-warm), transparent 70%),
      radial-gradient(ellipse 300px 260px at 760px 80px, var(--wash-ember), transparent 70%),
      radial-gradient(ellipse 280px 220px at 420px 300px, var(--wash-warm), transparent 72%),
      radial-gradient(ellipse 300px 260px at 780px 720px, var(--wash-ember), transparent 70%),
      radial-gradient(ellipse 340px 260px at 100px 1120px, var(--wash-warm), transparent 70%),
      radial-gradient(ellipse 300px 240px at 760px 1150px, var(--wash-warm), transparent 70%),
      linear-gradient(160deg, var(--wash-light), var(--paper));
  }
  .headlines { position: absolute; inset: 0; }
  .headline-text {
    font-family: "Josefin Sans", sans-serif;
    font-weight: 600;
    fill: var(--headline);
    filter: drop-shadow(1px 2px 1px var(--headline-shadow));
  }
  .turn-arrow { filter: drop-shadow(1px 2px 1px var(--headline-shadow)); }
  .divider {
    position: absolute;
    left: 0; top: 595px;
    width: 849px; height: 2px;
    background: var(--divider);
  }
  .logo {
    position: absolute;
    left: 24px; top: 648px;
    width: 412px; height: 412px;
    display: flex;
    flex-direction: column;
    align-items: center;
    justify-content: center;
    gap: 18px;
  }
  .logo-mark {
    width: 90px; height: 90px;
    border-radius: 50%;
    background: var(--logo-fill);
  }
  .logo-name {
    font-weight: 600;
    font-size: 34px;
    color: var(--logo-name);
  }
  .message {
    position: absolute;
    left: 488px; top: 656px;
    width: 342px;
    font-weight: 400;
    font-size: 24px;
    line-height: 37.6px;
    color: var(--ink);
  }
  .message strong { font-weight: 700; }
</style>
</head>
<body>
<main class="postcard">
  <svg class="headlines" width="849" height="1200" viewBox="0 0 849 1200">
    <text class="headline-text" x="42" y="124" font-size="66" textLength="506" lengthAdjust="spacingAndGlyphs">HOW TO CHANGE</text>
    <text class="headline-text" x="44" y="284" font-size="128" textLength="748" lengthAdjust="spacingAndGlyphs">THE WORLD</text>
    <text class="headline-text" x="44" y="424" font-size="90" textLength="544" lengthAdjust="spacingAndGlyphs">IN ONE STEP</text>
    <rect x="160" y="435" width="201" height="5" fill="var(--headline)"/>
    <text class="headline-text" x="42" y="560" font-size="62" textLength="460" lengthAdjust="spacingAndGlyphs">IT'S UP TO YOU...</text>
    <g class="turn-arrow" fill="var(--headline)">
      <path d="M708 364 C640 392 580 440 582 482 C584 518 640 526 740 514 L742 530 C630 548 564 536 560 486 C556 432 630 380 708 364 Z"/>
      <path d="M728 470 L808 512 L700 570 L728 522 Z"/>
    </g>
    <text class="headline-text" x="44" y="1164" font-size="72" textLength="764" lengthAdjust="spacing">PLEASE JOIN US!</text>
  </svg>

  <div class="divider"></div>

  <div class="logo">
    <div class="logo-mark"></div>
    <div class="logo-name">Live Ever Kinder</div>
  </div>

  <p class="message">You're going to spend your entire life with someone you can never get away from. (Guess who?) Wouldn't you rather that person #LiveEverKinder than judgmental or critical? BE the change you want to see! Visit <strong>www.LiveEverKinder-hub.com</strong> for daily Bright Pebbles and community.</p>
</main>
</body>
</html>
```